WE are a specialised tutoring business looking to a have a landing page design

we need a landing page designed for our business. We provide specialised tutoring for children with learning difficulties. I have attached a brief which includes our logo and also the content for the page.

Target Market(s)

parents

Number of Pages Required

1 page

Requirements
Must have
• our existing logo and the content provided

```html
<!DOCTYPE html>
<html lang="en">
<head>
<meta charset="utf-8">
<title>brightnest – specialised learning for children</title>
<link rel="stylesheet" href="https://fonts.googleapis.com/css2?family=Lato:wght@400;700&family=Open+Sans:wght@400;600&family=Roboto:wght@400&display=swap">
<style>
:root{
  --green:#5aa81e;
  --green-light:#8cc63f;
  --green-text:#4cae14;
  --ink:#111111;
  --text:#333333;
  --muted:#555555;
  --footer:#f2f2f2;
  --white:#ffffff;
}
*{margin:0;padding:0;box-sizing:border-box}
html,body{width:928px;height:1200px;overflow:hidden;background:var(--white)}
.page{position:relative;width:928px;height:1200px;font-family:"Open Sans",sans-serif;color:var(--text)}
.bg{position:absolute;left:0;top:0}
.brand{position:absolute;left:126px;top:18px;display:flex;align-items:center;gap:10px}
.brand-dot{width:36px;height:36px;border-radius:50%;background:var(--ink)}
.brand-name{font-family:"Lato",sans-serif;font-weight:700;font-size:26px;color:var(--green)}
.nav{position:absolute;top:25px;left:430px;display:flex;gap:32px;font-family:"Roboto",sans-serif;font-size:14.5px;color:var(--ink)}
.nav .active{color:var(--green-text)}
.search{position:absolute;left:774px;top:28px}
.hero-art{position:absolute;left:70px;top:142px;width:368px;height:255px;border-radius:6px;background:#e8e8e8;border:2px solid #d4d4d4;padding:10px 22px}
.hero-art-screen{width:100%;height:100%;background:linear-gradient(135deg,#ffffff,#d9d9d9)}
.hero-title{position:absolute;left:466px;top:158px;width:395px;font-family:"Lato",sans-serif;font-weight:700;font-size:19.5px;line-height:24px;color:var(--white)}
.field{position:absolute;top:298px;width:189px;height:39px;background:var(--white);font-size:12.5px;color:#666;padding:11px 15px}
.cta{position:absolute;left:469px;top:350px;width:218px;height:40px;background:var(--ink);color:var(--white);font-family:"Lato",sans-serif;font-size:14.5px;display:flex;align-items:center;justify-content:center}
.feature{position:absolute;top:454px;width:220px;text-align:center}
.feature-icon{width:100px;height:100px;border-radius:50%;border:5px solid var(--white);margin:0 auto}
.feature-title{margin-top:22px;font-family:"Lato",sans-serif;font-weight:700;font-size:17.6px;color:var(--ink)}
.feature-text{margin-top:10px;font-size:11.2px;line-height:15px;color:var(--muted);height:60px}
.more{display:inline-block;margin-top:14px;width:117px;height:33px;border:1.5px solid var(--green);color:var(--green-text);font-family:"Lato",sans-serif;font-weight:700;font-size:12px;line-height:30px}
.stat{position:absolute;top:842px;width:200px;text-align:center;font-family:"Lato",sans-serif;font-weight:700}
.stat-num{font-size:35px;line-height:40px;color:var(--green-text)}
.stat-label{font-size:15px;color:var(--white)}
.contact{position:absolute;top:1044px;font-size:12px;line-height:22px;color:var(--muted)}
.contact h3{font-family:"Open Sans",sans-serif;font-weight:600;font-size:13px;color:var(--ink);margin-bottom:2px}
.socials{display:flex;gap:20px;margin-top:6px}
.socials span{width:16px;height:16px;border-radius:50%;background:var(--ink)}
.copyright{position:absolute;top:1163px;width:100%;text-align:center;font-size:11px;color:var(--text);padding-left:-30px}
</style>
</head>
<body>
<div class="page">
  <svg class="bg" width="928" height="1200" viewBox="0 0 928 1200">
    <defs>
      <linearGradient id="heroGreen" x1="0" y1="0" x2="0" y2="1">
        <stop offset="0" stop-color="#8cc63f"/>
        <stop offset="1" stop-color="#5aa81e"/>
      </linearGradient>
    </defs>
    <path d="M0 108 Q464 36 928 108 L928 444 Q464 564 0 444 Z" fill="url(#heroGreen)"/>
    <rect x="0" y="768" width="928" height="300" fill="#151515"/>
    <path d="M0 1036 Q464 956 928 1036 L928 1148 L0 1148 Z" fill="#f2f2f2"/>
  </svg>

  <header>
    <div class="brand"><span class="brand-dot"></span><span class="brand-name">brightnest</span></div>
    <nav class="nav"><span class="active">Home</span><span>About us</span><span>Services</span><span>Contact Us</span></nav>
    <svg class="search" width="15" height="15" viewBox="0 0 15 15"><circle cx="6" cy="6" r="4.5" fill="none" stroke="#999" stroke-width="2"/><line x1="9.5" y1="9.5" x2="14" y2="14" stroke="#999" stroke-width="2.2"/></svg>
  </header>

  <section class="hero">
    <div class="hero-art"><div class="hero-art-screen" role="img" aria-label="Line illustration of learning tools, books, globe and study items shown on a tablet"></div></div>
    <h1 class="hero-title">Brightnest is a team of psychologists and teachers focused on supporting children with social, emotional, and learning difficulties. We provide specialised tutoring and support for children and their families.</h1>
    <div class="field" style="left:466px">Email address</div>
    <div class="field" style="left:664px">Phone Number</div>
    <div class="cta">I would like to know more</div>
  </section>

  <section class="features">
    <div class="feature" style="left:116px">
      <div class="feature-icon" style="background:var(--ink)" role="img" aria-label="Icon of a head with a thought bubble"></div>
      <h2 class="feature-title">Know the Child</h2>
      <p class="feature-text">We are dedicated to evidence-based assessment and diagnosis. We believe that early intervention requires a clear understanding of the unique challenges</p>
      <span class="more">READ MORE</span>
    </div>
    <div class="feature" style="left:351px">
      <div class="feature-icon" style="background:var(--green)" role="img" aria-label="Icon of a student reading a book"></div>
      <h2 class="feature-title">Meet the Need</h2>
      <p class="feature-text">We provide individualised tutoring for children that focuses on their specific areas of learning need. Our team are dedicated to providing best-practice</p>
      <span class="more">READ MORE</span>
    </div>
    <div class="feature" style="left:584px">
      <div class="feature-icon" style="background:var(--green-light)" role="img" aria-label="Icon of a growing plant"></div>
      <h2 class="feature-title">Watch them Grow</h2>
      <p class="feature-text">We are committed to seeing growth, this requiring strategic intervention and the ability to assess and provide evidence of achievement.</p>
      <span class="more">READ MORE</span>
    </div>
  </section>

  <section class="stats">
    <div class="stat" style="left:92px"><div class="stat-num">25k</div><div class="stat-label">Lorem ipsum dolor</div></div>
    <div class="stat" style="left:277px"><div class="stat-num">120k</div><div class="stat-label">Duis non nunc Nulla</div></div>
    <div class="stat" style="left:467px"><div class="stat-num">15k</div><div class="stat-label">Praesent metus</div></div>
    <div class="stat" style="left:642px"><div class="stat-num">189k</div><div class="stat-label">Quisque dignissim</div></div>
  </section>

  <footer>
    <div class="contact" style="left:167px"><h3>Email address</h3><p>info@brightnest.example</p></div>
    <div class="contact" style="left:397px"><h3>Address</h3><p>12/40 Harbour View Road,<br>Seabrook, 2190</p></div>
    <div class="contact" style="left:606px"><h3>Get in Touch</h3><div class="socials"><span></span><span></span><span></span><span></span></div></div>
    <p class="copyright">© 2019 Company Name&nbsp; All right reserved</p>
  </footer>
</div>
</body>
</html>
```